Design a styled business card for an intimacy and attachment psychologist

I am a Psychologist providing online therapy to patients across the United States. My work is interpersonal and emotion-focused, with an emphasis on the client-therapist relationship. My primary areas of work are very personal, including sexuality and gender, abuse and trauma, and grief and loss. My target audience will be adults of all ages 18+.
My business card should convey a warm and inviting feeling of professionalism that is also casual and comfortable.
The front should be fairly simple and professional, consisting of:
- My name, Dr. Rosalind Petrakis
- My title, Licensed Psycholigist
- My logo
On either the front or the back, my contact information should be listed:
- ros@drrospetrakis.example
- 555.014.7788
- drrospetrakis.example
On the rear, I would like a description of the areas that I specialize in. This can be formatted in any way that appears stylistically interesting.
Individual and Couples
Relationships and Infidelity
Sexual Health & Aging
Gender Identity & Sexual Orientation
Abuse and Trauma
Sexual Compulsivity & Addiction
Sexual Dysfunction
Target Market(s)
My target audience will be adults of all ages 18+.
Industry/Entity Type
Psychology
Contact Information for Business Card
The front should be fairly simple and professional, consisting of: - My name, Dr. Rosalind Petrakis - My title, Licensed Psycholigist - My logo On either the front or the back, my contact information should be listed: - ros@drrospetrakis.example - 555.014.7788 - drrospetrakis.example On the rear, I would like a description of the areas that I specialize in. This can be formatted in any way that appears stylistically interesting. Individual and Couples Relationships and Infidelity Sexual Health & Aging Gender Identity & Sexual Orientation Abuse and Trauma Sexual Compulsivity & Addiction Sexual Dysfunction
- Follow brand guide

```html
<!DOCTYPE html>
<html lang="en">
<head>
<meta charset="utf-8">
<title>Dr. Rosalind Petrakis — Business Card</title>
<link rel="stylesheet" href="https://fonts.googleapis.com/css2?family=Raleway:wght@300;400;500;600&display=swap">
<style>
  :root {
    --stage-light: #ffffff;
    --stage-edge: #ececec;
    --card-white: #ffffff;
    --ink-purple: #2a2549;
    --ink-text: #2f2b3f;
    --mark-teal: #4fcfb0;
    --ring-light: #f1f1f4;
    --ring-dark: #382f6c;
    --label-ink: #111111;
  }
  * { box-sizing: border-box; margin: 0; padding: 0; }
  html, body { width: 1200px; height: 470px; overflow: hidden; }
  body {
    position: relative;
    font-family: "Raleway", sans-serif;
    background: radial-gradient(ellipse at 50% 50%, var(--stage-light) 0%, var(--stage-light) 30%, var(--stage-edge) 100%);
  }
  .card {
    position: absolute;
    top: 93px;
    width: 431px;
    height: 247px;
    overflow: hidden;
    box-shadow: 0 10px 8px -6px rgba(0,0,0,0.35);
  }
  .card--front { left: 87px; background: var(--card-white); }
  .card--back { left: 682px; background: var(--ink-purple); }
  .card__ring { position: absolute; left: 0; top: 0; }

  .brand { position: absolute; left: 34px; top: 96px; display: flex; align-items: center; gap: 10px; }
  .brand__dot { width: 56px; height: 56px; border-radius: 50%; background: var(--mark-teal); flex: none; }
  .brand__name {
    font-weight: 600; font-size: 18px; line-height: 21px;
    color: var(--ink-purple); letter-spacing: 0.2px;
  }
  .title {
    position: absolute; left: 273px; top: 117px;
    font-size: 10.5px; font-weight: 400; color: var(--ink-text);
  }
  .contact {
    position: absolute; left: 77px; top: 205px;
    font-size: 10.5px; color: var(--ink-text); white-space: nowrap;
  }
  .contact__phone { letter-spacing: 2.6px; font-weight: 400; }
  .contact__sep { color: var(--ink-purple); margin: 0 9px 0 6px; }
  .contact__user { font-weight: 300; }
  .contact__domain { font-weight: 500; }

  .specialties {
    position: absolute; left: 0; right: 0; top: 52px;
    list-style: none; text-align: center;
    color: var(--card-white); font-size: 10.3px; font-weight: 400;
  }
  .specialties li { height: 20.6px; line-height: 20.6px; }

  .side-label {
    position: absolute; top: 381px; width: 120px; margin-left: -60px;
    text-align: center; font-size: 13px; font-weight: 500; color: var(--label-ink);
  }
  .side-label--front { left: 301px; }
  .side-label--back { left: 897px; }
</style>
</head>
<body>
  <section class="card card--front" aria-label="Card front">
    <svg class="card__ring" width="431" height="247" aria-hidden="true">
      <circle cx="308" cy="124" r="116" fill="none" stroke="var(--ring-light)" stroke-width="9"/>
    </svg>
    <div class="brand">
      <span class="brand__dot"></span>
      <span class="brand__name">Dr. Rosalind<br>Petrakis</span>
    </div>
    <p class="title">Licensed Psychologist</p>
    <p class="contact">
      <span class="contact__phone">+1.555.014.7788</span><span class="contact__sep">|</span><span class="contact__user">ros@</span><span class="contact__domain">drrospetrakis.example</span>
    </p>
  </section>

  <section class="card card--back" aria-label="Card back">
    <svg class="card__ring" width="431" height="247" aria-hidden="true">
      <circle cx="308" cy="124" r="116" fill="none" stroke="var(--ring-dark)" stroke-width="9"/>
    </svg>
    <ul class="specialties">
      <li>Individual and Couples</li>
      <li>Relationships and Infidelity</li>
      <li>Sexual Health &amp; Aging</li>
      <li>Gender Identity &amp; Sexual Orientation</li>
      <li>Abuse and Trauma</li>
      <li>Sexual Compulsivity &amp; Addiction</li>
      <li>Sexual Dysfunction</li>
    </ul>
  </section>

  <p class="side-label side-label--front">FRONT</p>
  <p class="side-label side-label--back">BACK</p>
</body>
</html>
```